Startup Jewelry Needs a fully coded Ecommerce Website

Description

We want the full coded woocommerce website - website to be operational and fully integrated with Quidora and other gateways .
We sell jewelry items like rings,ear rings,chain, necklaces etc.

Color Preference
Colors to be used are Velvet red, Black / anthracite, exclusive colors, silver-white, bronze-brown and golden.

Functionalities
Regarding Functions, the store will have functions of typical ecommerce jewelry store using the products/categories for the starting page, going into individual product pages by clicking these images and then leading to a detailed page for one product only.

Target Market
Jewelry-lovers, who appreciate extraordinary things, creative economy/fashion-industries, stylists, Style consultants, outfitter, theaters, operas, production sites, Cocktail-, Dinner and Bride-fashion etc

Look and Feel
Each slider illustrates characteristics of the customer's brand and the style your web design should communicate.

Must have
Logo must be designed

Should Not Have:
- - Dull and common design
- - Messy/unstructured navigation

Industry/Entity Type

Jewelry

Coding

Coded - Design and coding required

```html
<!DOCTYPE html>
<html lang="en">
<head>
<meta charset="utf-8">
<title>Jewel Orbit – Shop</title>
<link href="https://fonts.googleapis.com/css2?family=Raleway:wght@400;500;600&display=swap" rel="stylesheet">
<style>
:root{
  --stage:#1f211f;
  --page:#ffffff;
  --ink:#333a40;
  --muted:#8a8f94;
  --line:#e3e5e8;
  --rule:#3b4148;
  --sale:#e4553a;
  --green:#6cc47a;
  --gold:#b08a3a;
  --footer:#36414d;
  --footer-line:#55606c;
}
*{box-sizing:border-box;margin:0;padding:0}
html,body{width:1200px;height:2571px;overflow:hidden}
body{background:var(--stage);font-family:"Raleway",sans-serif;color:var(--ink);position:relative}
.page{position:absolute;left:69px;top:146px;width:1059px;height:2266px;background:var(--page)}
.abs{position:absolute}

/* header */
.logo{left:51px;top:22px;display:flex;align-items:center;gap:10px}
.logo-mark{width:44px;height:44px;border:2px solid var(--gold)}
.logo-name{font-size:24px;font-weight:600;color:var(--gold)}
.search{left:310px;top:34px;width:380px;height:31px;border:1px solid var(--line);display:flex}
.search span{flex:1;font-size:11px;color:var(--muted);padding:9px 10px}
.search i{width:36px;border-left:1px solid var(--line);display:flex;align-items:center;justify-content:center}
.cart{left:949px;top:27px;display:flex;align-items:center;gap:5px;font-size:11px;color:var(--ink)}
.cart b{background:var(--sale);color:#fff;font-weight:400;font-size:10px;padding:1px 5px}
.nav{left:44px;top:113px;width:969px;height:23px;border-bottom:2px solid var(--rule);display:flex;gap:26px;padding-left:10px}
.nav a{font-size:11px;color:var(--ink);text-decoration:none;text-transform:uppercase}
.offers{left:44px;top:145px;width:969px;display:flex}
.offer{flex:1;text-align:center;border-right:1px solid var(--line)}
.offer:last-child{border-right:0}
.offer h3{font-size:12px;font-weight:500;text-transform:uppercase}
.offer p{font-size:9px;color:var(--muted);text-transform:uppercase;margin-top:4px}

/* banners */
.banners{left:44px;top:196px;display:flex;gap:24px}
.banner{width:307px;height:202px;position:relative;color:#fff}
.banner .photo{position:absolute;inset:0}
.banner h2{position:absolute;left:16px;font-size:21px;font-weight:500;line-height:1.2;text-transform:uppercase}
.btn{position:absolute;left:16px;background:var(--green);color:#fff;font-size:11px;text-transform:uppercase;width:108px;height:31px;display:flex;align-items:center;justify-content:center}

/* sidebar */
.widget{left:44px;width:223px;border:1px solid var(--line)}
.widget h4{font-size:14px;font-weight:500;text-transform:uppercase;padding:10px 12px;border-bottom:1px solid var(--line)}
.widget li{list-style:none;font-size:11px;padding:10px 12px;border-bottom:1px solid var(--line)}
.widget li:last-child{border-bottom:0}
.range{position:relative;height:60px;margin:0 14px}
.range .track{position:absolute;left:4px;right:4px;top:33px;height:2px;background:var(--rule)}
.range .knob{position:absolute;top:29px;width:9px;height:9px;border:1px solid var(--rule);background:#fff}
.range .knob.end{right:0;background:var(--green);border-color:var(--green)}
.price-row{display:flex;align-items:center;gap:8px;padding:0 12px 12px}
.price-row span{width:60px;height:31px;border:1px solid var(--line);font-size:10px;color:var(--muted);display:flex;align-items:center;justify-content:center}
.price-row em{font-style:normal;font-size:10px;color:var(--muted)}
.filter{background:var(--green);color:#fff;font-size:13px;font-weight:500;padding:8px 6px}

/* products */
.sort{left:872px;top:454px;width:141px;height:19px;border:1px solid #bfc3c7;font-size:10px;padding:3px 5px;color:var(--ink)}
.sort i{position:absolute;right:1px;top:1px;width:13px;height:15px;background:#e8e8e8;border-left:1px solid #bfc3c7}
.grid{left:293px;top:490px;display:grid;grid-template-columns:repeat(3,224px);grid-auto-rows:357px;column-gap:24px;row-gap:46px}
.card{border:1px solid var(--line);padding:11px 11px 0;text-align:center;position:relative}
.card .photo{height:282px}
.sale{position:absolute;right:20px;top:20px;width:50px;height:50px;border-radius:50%;background:var(--sale);color:#fff;font-size:11px;display:flex;align-items:center;justify-content:center}
.card h5{font-size:11px;font-weight:400;color:var(--muted);line-height:1.7;margin-top:8px;padding:0 6px}
.price{font-size:14px;margin-top:2px}
.price s{color:var(--muted);margin-right:4px}

/* features */
.features{left:44px;top:2127px;display:flex;gap:24px}
.feature{width:307px;height:98px;border:1px solid var(--line);display:flex;gap:14px;padding:14px 18px}
.feature h6{font-size:16px;font-weight:500;margin-bottom:6px}
.feature p{font-size:11px;color:var(--muted);line-height:1.7}

/* footer */
.footer{position:absolute;left:69px;top:2412px;width:1059px;height:139px;background:var(--footer)}
.pay{left:45px;top:34px;display:flex;gap:9px}
.pay span{width:51px;height:31px;border-radius:3px;background:#fff;font-size:10px;font-weight:600;color:var(--footer);display:flex;align-items:center;justify-content:center}
.divider{left:704px;top:30px;width:1px;height:40px;background:var(--footer-line)}
.social{left:773px;top:38px;display:flex;gap:10px}
.social span{width:31px;height:31px}
.hr{left:45px;top:99px;width:969px;height:1px;background:var(--footer-line)}
.copy{left:0;top:117px;width:100%;text-align:center;font-size:10px;color:#c7ccd1}
.copy b{color:var(--green);font-weight:400}
</style>
</head>
<body>
<main class="page">
  <header>
    <div class="abs logo"><span class="logo-mark"></span><span class="logo-name">Jewel Orbit</span></div>
    <div class="abs search"><span>Search Products...</span><i><svg width="13" height="13" viewBox="0 0 13 13"><circle cx="5.5" cy="5.5" r="4.3" fill="none" stroke="#333a40" stroke-width="1.8"/><line x1="8.6" y1="8.6" x2="12" y2="12" stroke="#333a40" stroke-width="2"/></svg></i></div>
    <div class="abs cart"><svg width="14" height="12" viewBox="0 0 14 12"><path d="M0 1h2.5l2 7h7l2-5H4" fill="none" stroke="#333a40" stroke-width="1.4"/><circle cx="5.5" cy="10.5" r="1.2" fill="#333a40"/><circle cx="10.5" cy="10.5" r="1.2" fill="#333a40"/></svg>CART <b>0</b></div>
    <nav class="abs nav"><a>Home</a><a>Shop</a><a>Rings</a><a>Earrings</a><a>Necklace</a><a>Chain</a></nav>
    <div class="abs offers">
      <div class="offer"><h3>Save 18% now</h3><p>Coupon code: EC02142</p></div>
      <div class="offer"><h3>Discount up to 25%</h3><p>Buy more save more. Coupon code: EC02142</p></div>
      <div class="offer"><h3>Get additional 10%</h3><p>For new customers, coupon code: EC02142</p></div>
    </div>
  </header>

  <section class="abs banners">
    <div class="banner"><div class="photo" role="img" aria-label="Diamond necklace on a dark velvet bust" style="background:radial-gradient(circle at 55% 50%,#6b6f74,#1c1d20 70%)"></div><h2 style="top:58px">Diamond Collection</h2><span class="btn" style="top:110px">Shop now</span></div>
    <div class="banner" style="height:206px"><div class="photo" role="img" aria-label="Two gold wedding rings on red fabric" style="background:radial-gradient(circle at 60% 60%,#e0453c,#a9121a 80%)"></div><h2 style="top:17px">Save 25%<br>on wedding rings</h2><span class="btn" style="top:96px">Shop now</span></div>
    <div class="banner" style="height:206px"><div class="photo" role="img" aria-label="Diamond cluster ear rings on black" style="background:radial-gradient(circle at 70% 50%,#5a5c60,#0d0d0f 65%)"></div><h2 style="top:17px">10%<br>Discount on ear rings</h2><span class="btn" style="top:96px">Shop now</span></div>
  </section>

  <aside>
    <div class="abs widget" style="top:454px"><h4>Product Categories</h4><ul><li>Chain</li><li>Ear Rings</li><li>Necklace</li><li>Rings</li></ul></div>
    <div class="abs widget" style="top:651px"><h4>Price Range</h4>
      <div class="range"><span class="track"></span><span class="knob" style="left:0"></span><span class="knob end"></span></div>
      <div class="price-row"><span>$13</span><em>—</em><span>$189</span><b class="filter">FILTER</b></div>
    </div>
  </aside>

  <div class="abs sort">Default sorting<i></i></div>

  <section class="abs grid">
    <article class="card"><div class="photo" role="img" aria-label="White gold heart diamond pendant" style="background:linear-gradient(#f4f6f8,#dfe4e8)"></div><span class="sale">SALE!</span><h5>14 Karat White Gold Heart Diamond Pendant</h5><p class="price"><s>$159.99</s>$139.99</p></article>
    <article class="card"><div class="photo" role="img" aria-label="Antique gold plated earrings on pale blue" style="background:linear-gradient(#c9d3ea,#aebcdc)"></div><span class="sale">SALE!</span><h5>Antique-Style Gold Plated Copper Earrings</h5><p class="price"><s>$20.99</s>$17.99</p></article>
    <article class="card"><div class="photo" role="img" aria-label="Gold ring with crystal flower setting" style="background:radial-gradient(circle,#d9c27a,#d7eef0 70%)"></div><span class="sale">SALE!</span><h5>CZ Embellished Ring</h5><p class="price"><s>$69.00</s>$49.00</p></article>
    <article class="card"><div class="photo" role="img" aria-label="Silver nail ring on black" style="background:radial-gradient(circle,#8a8c90,#050505 60%)"></div><span class="sale">SALE!</span><h5>Designer Silver Nail Ring With Cubic Zircons</h5><p class="price"><s>$109.99</s>$89.99</p></article>
    <article class="card"><div class="photo" role="img" aria-label="Engraved gold necklace set with earrings" style="background:radial-gradient(circle,#d59a2a,#f1ede6 75%)"></div><span class="sale">SALE!</span><h5>Gold Plated Designer Engraved Necklace Set With Earrings</h5><p class="price"><s>$159.00</s>$119.00</p></article>
    <article class="card"><div class="photo" role="img" aria-label="Gold leaf pearl drop earrings on dark grey" style="background:radial-gradient(circle,#8c8a86,#3a3a3a 70%)"></div><span class="sale">SALE!</span><h5>Gold Plated Pearl Drop Earrings</h5><p class="price"><s>$150.00</s>$119.00</p></article>
    <article class="card"><div class="photo" role="img" aria-label="Crystal bridal earrings worn by a model" style="background:linear-gradient(90deg,#d9b8a0,#b57f5c)"></div><span class="sale">SALE!</span><h5>Corvelle Austrian Crystal Bridal Earrings</h5><p class="price"><s>$16.99</s>$13.99</p></article>
    <article class="card"><div class="photo" role="img" aria-label="Long diamond necklace on a black bust" style="background:radial-gradient(circle,#6b6d70,#0b0b0c 65%)"></div><span class="sale">SALE!</span><h5>Long Diamond Necklace With Earrings</h5><p class="price"><s>$219.99</s>$189.99</p></article>
    <article class="card"><div class="photo" role="img" aria-label="Sterling silver chain on white" style="background:linear-gradient(#ffffff,#eef0f2)"></div><span class="sale">SALE!</span><h5>Sterling Silver Rhodium Plated Chain</h5><p class="price"><s>$39.00</s>$29.00</p></article>
    <article class="card"><div class="photo" role="img" aria-label="Pink and silver leaf earrings on black" style="background:radial-gradient(circle,#c88d84,#080808 55%)"></div><span class="sale">SALE!</span><h5>Zircon Encrusted Silver Pink Pearl Earrings</h5><p class="price"><s>$229.00</s>$161.99</p></article>
  </section>

  <section class="abs features">
    <div class="feature"><svg width="26" height="30" viewBox="0 0 26 30"><path d="M6 13V9a7 7 0 0 1 14 0v4" fill="none" stroke="#4a525a" stroke-width="3.5"/><rect x="2" y="13" width="22" height="16" rx="2" fill="#4a525a"/></svg><div><h6>Secure Payments</h6><p>Lorem ipsum dolor sit amet. Morbi at nisl lorem, vel porttitor justo.</p></div></div>
    <div class="feature"><svg width="22" height="34" viewBox="0 0 22 34"><text x="11" y="29" text-anchor="middle" font-family="Raleway,sans-serif" font-size="34" font-weight="600" fill="#4a525a">$</text></svg><div><h6>Money Back Guarantee</h6><p>Lorem ipsum dolor sit amet. Morbi at nisl lorem, vel porttitor justo.</p></div></div>
    <div class="feature"><svg width="38" height="28" viewBox="0 0 38 28"><rect x="12" y="2" width="25" height="18" fill="#4a525a"/><path d="M12 8H5L1 14v6h11z" fill="#4a525a"/><circle cx="8" cy="22" r="4" fill="#4a525a" stroke="#fff" stroke-width="1.5"/><circle cx="29" cy="22" r="4" fill="#4a525a" stroke="#fff" stroke-width="1.5"/></svg><div><h6>Free Delivery</h6><p>Pellentesque habitant morbi netus tristique senectus et malesuada.</p></div></div>
  </section>
</main>

<footer class="footer">
  <div class="abs pay"><span>Quidora</span><span>Tallon</span><span>Brisk</span><span>Merit</span><span>Ferro</span></div>
  <span class="abs divider"></span>
  <div class="abs social">
    <span style="background:#3b5998" aria-label="Social link"></span>
    <span style="background:#1da1f2" aria-label="Social link"></span>
    <span style="background:#0e76a8" aria-label="Social link"></span>
    <span style="background:#dd4b39" aria-label="Social link"></span>
    <span style="background:#ff0084" aria-label="Social link"></span>
    <span style="background:#cb2027" aria-label="Social link"></span>
  </div>
  <span class="abs hr"></span>
  <p class="abs copy"><b>Jewel Orbit</b> Copyright © 2016. Web Design by <b>Studio Lumen</b></p>
</footer>
</body>
</html>
```